Hi,
We are also sourcing for a logo, if you have ideas please take a look at our other project (if you look at our profile you should be able to see it).
We are looking for a website that will be used to manage mobile devices. The feature set is rather small, users can Wipe, Lock, Locate devices as well as make them Ring or Speak (by sending text to be spoken). We attached some images of what it looks like right now. We are looking for simplicity, uniformity and most importantly, the website should be thought of as primary User Interface, it should flow.
Please see attached to get an idea of what it looks like now. The current design was inspired by making a site that will work and flow well on a variety of displays (from mobile to tablet to desktop).
We want to stay away from radio buttons, check-boxes. This should be engaging and creative, opposite of Corporate. Not busy (ideally we are looking to have fewest possible choices at any given time and at the same time no feature should be more than 3 clicks away (this is a suggestion/approximation... just want to share our understanding of what 'flow' is).
Could be cartoony.
Thanks!
BrambleKeep
Reason: there are a couple of designs that are interesting, in addition to specific feedback I provided, possibly looking for more concepts.
Thank You

```html
<!DOCTYPE html>
<html lang="en">
<head>
<meta charset="utf-8">
<title>BrambleKeep – Lost Your Phone?</title>
<link href="https://fonts.googleapis.com/css2?family=Federo&family=Caveat:wght@600&family=Roboto+Condensed:wght@400&family=Arimo:wght@400;700&display=swap" rel="stylesheet">
<style>
:root{
  --sky:#5ea7cf;
  --sky-dark:#4a98c4;
  --ink:#4d4d4d;
  --body:#666;
  --rule:#d6d6d6;
  --footer:#333;
  --footer-text:#ddd;
}
*{box-sizing:border-box;margin:0;padding:0}
html,body{width:880px;height:1200px;overflow:hidden;background:#fff}
body{position:relative;font-family:"Arimo",Arial,sans-serif;color:var(--body)}
.abs{position:absolute}
.display{font-family:"Federo",sans-serif}

/* top navigation */
.topnav{left:0;top:0;width:880px;height:44px;background:var(--sky)}
.topnav a{position:absolute;top:12px;font-family:"Federo",sans-serif;font-size:14.5px;color:#fff;text-decoration:none;letter-spacing:.3px}
.topnav .current::after{content:"";position:absolute;left:50%;bottom:-12px;margin-left:-5px;border:5px solid transparent;border-bottom-color:#fff}
.search{left:667px;top:14px;width:118px;height:17px;background:#fff}
.search svg{position:absolute;right:5px;top:3px}
.utility a{position:absolute;top:52px;font-size:10px;color:#888;text-decoration:none}

/* brand: plain text name in body font with a single plain circle */
.brand{left:0;width:880px;top:76px;display:flex;align-items:center;justify-content:center;gap:8px;font-family:"Arimo",Arial,sans-serif;font-weight:400;font-size:26px;color:var(--ink)}
.brand-dot{width:12px;height:12px;border-radius:50%;background:var(--sky)}
.headline{left:0;width:892px;top:162px;text-align:center;font-size:32px;font-weight:400;color:var(--ink)}

.feature{top:240px;display:flex;align-items:center;gap:8px;font-family:"Caveat",cursive;font-size:28px;color:#333}
.ring-icon{width:28px;height:28px;border-radius:50%;background:radial-gradient(circle,#fff 0 4px,var(--sky) 5px 9px,#fff 10px 11px,var(--sky) 12px 14px)}
.rule{height:2px;background:linear-gradient(90deg,rgba(200,200,200,0),#d2d2d2 20%,#d2d2d2 80%,rgba(200,200,200,0))}

.get-app{left:306px;top:318px;width:260px;height:61px;border-radius:31px;background:linear-gradient(#c9c9ca,#9fa0a2);border:3px solid #8e8f91;box-shadow:0 2px 3px rgba(0,0,0,.2)}
.get-app svg{position:absolute;left:2px;top:2px}
.get-app span{position:absolute;left:74px;top:11px;font-family:"Federo",sans-serif;font-size:27px;color:#fff;font-style:italic}

.section-title{left:84px;width:702px;display:flex;align-items:center;gap:14px;font-size:16px;letter-spacing:2px;color:var(--sky)}
.section-title i{flex:1;border-top:1px dashed #aaa}

.tile{width:102px;height:87px;border-radius:7px;background:linear-gradient(#e4e4e4 0%,#b9babc 42%,#8f9093 60%,#b8b9bb 100%);box-shadow:0 2px 3px rgba(0,0,0,.3);display:flex;align-items:center;justify-content:center;font-family:"Federo",sans-serif;font-size:21px;color:#fff;text-shadow:0 1px 2px rgba(0,0,0,.45)}
.tile.big{width:104px;height:88px;font-size:23px}
.warning{left:0;width:880px;top:596px;text-align:center;font-family:"Roboto Condensed",sans-serif;font-size:19px;color:var(--sky-dark)}

.col-title{top:801px;font-family:"Federo",sans-serif;font-size:17px;font-weight:400;color:#333}
.news{width:212px}
.news h3{font-size:10px;font-weight:700;color:#444;display:flex;align-items:center;gap:6px}
.tick{width:13px;height:13px;border-radius:50%;background:var(--sky);display:inline-flex;align-items:center;justify-content:center}
.news p{margin:6px 0 0 18px;font-size:8.6px;line-height:12.4px;text-align:justify;color:#777}
.map{left:549px;top:832px;width:256px;height:160px;border:3px solid #ddd;background:linear-gradient(135deg,#e9e6d9,#d7dccb 50%,#e6d7b0)}

/* footer */
.footer{left:0;top:1008px;width:880px;height:192px;background:var(--footer)}
.footer-title{position:absolute;font-size:11px;font-weight:400;color:#fff;letter-spacing:.3px}
.pill-btn{position:absolute;background:linear-gradient(#f1f1f1,#c9c9c9);border:1px solid #999;border-radius:3px;color:#222;font-size:8px;display:flex;align-items:center;justify-content:center}
.blog-post{position:absolute;left:69px;width:195px;font-size:7.8px;line-height:11px;text-align:justify;color:#ccc}
.blog-sep{position:absolute;left:69px;width:195px;border-top:1px solid #555}
.field{position:absolute;left:351px;width:200px;height:17px;background:#f4f4f4;border:1px solid #bbb;font-family:Georgia,serif;font-style:italic;font-size:8px;color:#888;padding:3px 8px}
.social{position:absolute;top:1157px;display:flex;align-items:center;gap:4px;font-size:8px;color:#fff}
.social b{width:9px;height:9px;background:var(--sky)}
.links a{position:absolute;left:670px;font-size:8px;color:var(--footer-text);text-decoration:none}
.copyright{left:581px;top:1159px;font-size:8px;color:#fff}
</style>
</head>
<body>

<nav class="abs topnav">
  <a class="current" style="left:94px">Home</a>
  <a style="left:166px">About Us</a>
  <a style="left:263px">Latest News</a>
  <a style="left:376px">Services</a>
  <a style="left:466px">Contact Us</a>
  <div class="abs search">
    <svg width="11" height="11" viewBox="0 0 11 11"><circle cx="4.5" cy="4.5" r="3.3" fill="none" stroke="#bbb" stroke-width="1.4"/><path d="M7 7l3 3" stroke="#bbb" stroke-width="1.6"/></svg>
  </div>
</nav>
<div class="utility">
  <a style="left:602px">admin</a>
  <a style="left:647px">device</a>
  <a style="left:698px">settings</a>
  <a style="left:749px">signout</a>
</div>

<div class="abs brand"><span class="brand-dot"></span>BrambleKeep</div>
<h1 class="abs headline display">Lost Your Phone?</h1>

<div class="abs feature" style="left:126px"><span class="ring-icon"></span>Wipe data</div>
<div class="abs feature" style="left:312px"><span class="ring-icon"></span>Lock it</div>
<div class="abs feature" style="left:469px"><span class="ring-icon"></span>Ring it</div>
<div class="abs feature" style="left:625px"><span class="ring-icon"></span>Find it</div>
<div class="abs rule" style="left:248px;top:295px;width:392px"></div>

<div class="abs get-app">
  <svg width="51" height="51" viewBox="0 0 51 51"><circle cx="25.5" cy="25.5" r="24" fill="#fff"/><circle cx="25.5" cy="25.5" r="20" fill="#9e9fa1"/><path d="M10 19h14v-9l17 15.5-17 15.5v-9H10z" fill="#fff"/></svg>
  <span>Get Me App</span>
</div>

<div class="abs section-title" style="top:416px"><i></i>OUR APPS<i></i></div>

<div class="abs tile" style="left:82px;top:465px">Wipe</div>
<div class="abs tile" style="left:204px;top:465px">Lock</div>
<div class="abs tile" style="left:330px;top:465px">Find</div>
<div class="abs tile" style="left:452px;top:465px">Ring</div>
<div class="abs tile" style="left:574px;top:465px">Speak</div>
<div class="abs tile" style="left:695px;top:465px">Loading</div>
<div class="abs rule" style="left:69px;top:582px;width:715px"></div>

<div class="abs warning">THIS WILL ERASE ALL YOUR FILES ON YOUR DEVICE</div>
<div class="abs tile big" style="left:312px;top:634px">Cancel</div>
<div class="abs tile big" style="left:435px;top:634px">Wipe</div>

<div class="abs section-title" style="top:749px"><i></i>CONTACTS<i></i></div>

<h2 class="abs col-title" style="left:67px">Latest News</h2>
<div class="abs news" style="left:67px;top:835px">
  <h3><span class="tick"><svg width="8" height="8" viewBox="0 0 8 8"><path d="M1 4l2 2 4-4.5" fill="none" stroke="#fff" stroke-width="1.5"/></svg></span>Lorem ipsum dolor sit amet</h3>
  <p>Lorem ipsum dolor sit amet, consectetur adipisicing elit, sed do eiusmod tempor incididunt ut labore et dolore magna aliqua. Ut enim ad minim veniam, quis nostrud exercitation ullamco laboris nisi ut aliquip ex ea commodo consequat</p>
</div>
<div class="abs news" style="left:294px;top:835px">
  <h3><span class="tick"><svg width="8" height="8" viewBox="0 0 8 8"><path d="M1 4l2 2 4-4.5" fill="none" stroke="#fff" stroke-width="1.5"/></svg></span>Lorem ipsum dolor sit amet</h3>
  <p>Lorem ipsum dolor sit amet, consectetur adipisicing elit, sed do eiusmod tempor incididunt ut labore et dolore magna aliqua. Ut enim ad minim veniam, quis nostrud exercitation ullamco laboris nisi ut aliquip ex ea commodo consequat</p>
</div>

<h2 class="abs col-title" style="left:547px">Trace the phonbe</h2>
<div class="abs map" role="img" aria-label="Street map showing the phone's last known location"></div>

<footer class="abs footer"></footer>
<h4 class="footer-title" style="left:69px;top:1024px">OUR BLOG</h4>
<div class="pill-btn" style="left:202px;top:1021px;width:61px;height:18px">FOLLOW US &gt;&gt;</div>
<p class="blog-post" style="top:1057px">Lorem ipsum dolor sit amet, consectetur adipisicing elit, sed do eiusmod tempor incididunt ut labore et dolore magna aliqua.</p>
<div class="blog-sep" style="top:1095px"></div>
<p class="blog-post" style="top:1103px">Lorem ipsum dolor sit amet, consectetur adipisicing elit, sed do eiusmod tempor incididunt ut labore et dolore magna aliqua.</p>
<div class="blog-sep" style="top:1142px"></div>
<p class="blog-post" style="top:1149px">Lorem ipsum dolor sit amet, consectetur adipisicing elit, sed do eiusmod tempor incididunt ut labore et dolore magna aliqua.</p>

<h4 class="footer-title" style="left:350px;top:1025px">QUICK CONTACT</h4>
<div class="field" style="top:1043px">Name</div>
<div class="field" style="top:1064px">Phone</div>
<div class="field" style="top:1086px">E-mail</div>
<div class="pill-btn" style="left:474px;top:1111px;width:74px;height:22px;font-size:9px">SUBMIT&gt;&gt;</div>

<div class="abs" style="left:353px;top:1157px;font-size:9px;font-weight:700;color:#fff">FOLLOW US</div>
<div class="social" style="left:422px"><b></b>Linkline</div>
<div class="social" style="left:472px"><b></b>Chirper</div>
<div class="social" style="left:520px"><b></b>Friendbook</div>

<div class="links">
  <a style="top:1028px">Terms and Conditions</a>
  <a style="top:1046px">Privacy Policy</a>
  <a style="top:1063px">Frequently Asked Questions</a>
  <a style="top:1081px">About Us</a>
  <a style="top:1098px">Our Services</a>
  <a style="top:1116px">Contact Us</a>
</div>
<div class="abs copyright">Copyright © 2012. BrambleKeep inc All rights reserved</div>

</body>
</html>
```